Business Card Design Project

I need a business card design for an Organic drive thru coffee kiosk. We will serve organic coffee, teas & smoothies and will serve healthy breakfast food/snacks for people on the go.
I want the card to have 2-3 colors max (earthy colors like browns, greens and so on).
I have attached the logo I want used and would love to play off the theme of "balance."
Include:
Tidy-Kettle Coffee
address: 4820 Gorvin Ct. Raleigh, NC 27583
phone: 919-731-4062
website: www.tidy-kettle.com (website is not up yet but still include it on card)
email: Rosalind@tidy-kettle.com
I want one of the following sayings somewhere on the card (the front or back is fine):
"Eat & Drink Well, on the run!"
"Break the fast with Tidy-Kettle"
Maybe on the back list what we offer:
-Organic coffee, espresso & tea
-Blendora smoothies & protein shakes
-Zesty Pour (100% fresh local fruit and veggies)
-Tender Nibs

```html
<!DOCTYPE html>
<html lang="en">
<head>
<meta charset="utf-8">
<title>Tidy-Kettle Coffee Business Cards</title>
<link rel="stylesheet" href="https://fonts.googleapis.com/css2?family=PT+Sans+Narrow:wght@400;700&display=swap">
<style>
  :root {
    --card-olive: #4b4230;
    --cream: #f7f3ea;
    --bean-brown: #6b2a1c;
    --backdrop: #e9e5de;
    --shadow: rgba(40, 30, 20, 0.28);
  }
  * { margin: 0; padding: 0; box-sizing: border-box; }
  html, body {
    width: 1200px;
    height: 1200px;
    overflow: hidden;
    background: var(--backdrop);
    font-family: "PT Sans Narrow", "Arial Narrow", sans-serif;
  }
  .sheet {
    position: relative;
    width: 1200px;
    height: 1200px;
  }
  .card {
    position: absolute;
    left: 250px;
    width: 700px;
    height: 400px;
    background: var(--card-olive);
    color: var(--cream);
    overflow: hidden;
    box-shadow: 0 10px 28px var(--shadow);
  }
  .card--front { top: 150px; }
  .card--back { top: 650px; }

  /* Front */
  .front-badge {
    position: absolute;
    left: -70px;
    top: -110px;
    width: 400px;
    height: 400px;
    border-radius: 50%;
    background: var(--cream);
    display: flex;
    align-items: center;
    justify-content: center;
    padding: 110px 0 0 70px;
  }
  .brand-name {
    font-size: 54px;
    font-weight: 400;
    color: var(--bean-brown);
    letter-spacing: 0.5px;
  }
  .front-rule {
    position: absolute;
    height: 4px;
    background: var(--cream);
  }
  .front-rule--upper { left: 40px; right: 0; top: 262px; }
  .front-rule--lower { left: 380px; right: 0; top: 368px; }
  .contact {
    position: absolute;
    right: 52px;
    top: 96px;
    text-align: right;
    font-size: 30px;
    line-height: 1.08;
  }
  .contact-web {
    position: absolute;
    right: 52px;
    top: 290px;
    font-size: 34px;
  }

  /* Back */
  .tagline {
    position: absolute;
    right: 118px;
    top: 34px;
    font-size: 40px;
    font-weight: 400;
  }
  .back-rule {
    position: absolute;
    left: 0;
    right: 90px;
    top: 96px;
    height: 4px;
    background: var(--cream);
  }
  .back-badge {
    position: absolute;
    right: 14px;
    top: 46px;
    width: 110px;
    height: 110px;
    border-radius: 50%;
    background: var(--cream);
    display: flex;
    align-items: center;
    justify-content: center;
  }
  .back-badge .brand-name { font-size: 20px; }
  .offer-list {
    position: absolute;
    left: 60px;
    right: 150px;
    top: 130px;
    list-style: none;
    text-align: center;
    font-size: 31px;
    line-height: 1.22;
  }
</style>
</head>
<body>
<main class="sheet">
  <section class="card card--front" aria-label="Business card front">
    <div class="front-badge">
      <span class="brand-name">Tidy-Kettle</span>
    </div>
    <address class="contact" style="font-style:normal">
      4820 Gorvin Ct. Raleigh,<br>
      NC 27583<br>
      919-731-4062<br>
      Rosalind@tidy-kettle.com
    </address>
    <div class="front-rule front-rule--upper"></div>
    <div class="contact-web">www.tidy-kettle.com</div>
    <div class="front-rule front-rule--lower"></div>
  </section>

  <section class="card card--back" aria-label="Business card back">
    <h2 class="tagline">Eat &amp; Drink Well, on the run!</h2>
    <div class="back-rule"></div>
    <div class="back-badge">
      <span class="brand-name">Tidy-Kettle</span>
    </div>
    <ul class="offer-list">
      <li>-Organic coffee, espresso &amp; tea</li>
      <li>-Blendora smoothies &amp; protein shakes</li>
      <li>-Zesty Pour</li>
      <li>(100% fresh local fruit and veggies)</li>
      <li>-Tender Nibs</li>
    </ul>
  </section>
</main>
</body>
</html>
```